RM Tomás Rivera (Business Card)

Hi designers, in this work, I'm looking for an sophisticated stylish, elegant and proffesional personal card. We have a laboratory of pathology automated, with equipments high quality.
In this web the designers, have created my business logo, the name is "RM Tomás Rivera"
In our lab, we principal work is to prepare the biopsies for further diagnostic of diseases like cancer, tumors, etc.
I need that the first face, only having my complete logo (Rm Tomás Rivera, Laboratorio de procesamiento Histologico)
The overleaf, could repeat the same logo, like water logo.
In this face, I need to say: My full data:

Técnico en Anatomía Patológica
Tomás Rivera Ibarra M.P 47203
Av. Paredes Luján 418 - 2do piso - Instituto Marbel.
Córdoba, Argentina
(0351) 154820937
rivera.tomas@correolab.example

with respect the colors of card, use your imagination, the original logo color is violet, I haven't chosen a color base for the card.

attached pictures are examples of cards I like your DESIGN.
Attached too, the original logo to my company.

the size of card are:
horizontal: 9cm
vertical: 5,5cm

any question that you have, not doubt to question me,
Hand to work!

Industry/Entity Type

Laboratory

Requirements
Must have
• designers sophisticated, not simples, like show the images attached

```html
<!DOCTYPE html>
<html lang="es">
<head>
<meta charset="utf-8">
<title>Tomás Rivera — Tarjeta personal</title>
<link rel="stylesheet" href="https://fonts.googleapis.com/css2?family=Roboto+Condensed:wght@400&family=Arimo:wght@400&display=swap">
<style>
  :root {
    --backdrop: #3b3f3e;
    --violet: #7a3fa6;
    --violet-light: #8c4fbb;
    --violet-dark: #6a3093;
    --grey-band: #8e8e92;
    --grey-band-light: #a9a9ad;
    --paper: #f6f6f4;
    --text-grey: #77777b;
    --mark-light: #ece6f2;
  }
  * { box-sizing: border-box; margin: 0; padding: 0; }
  html, body {
    width: 1200px;
    height: 900px;
    overflow: hidden;
    background: var(--backdrop);
  }
  .sheet {
    width: 1200px;
    height: 900px;
    display: flex;
    flex-direction: column;
    align-items: center;
    justify-content: center;
    gap: 40px;
  }
  .card {
    position: relative;
    width: 640px;
    height: 391px;
    overflow: hidden;
    box-shadow: 0 10px 30px rgba(0,0,0,0.35);
  }

  /* Front face */
  .card--front {
    background: linear-gradient(135deg, var(--violet-light) 0%, var(--violet) 55%, var(--violet-dark) 100%);
    display: flex;
    align-items: center;
    justify-content: center;
  }
  .brand {
    display: flex;
    flex-direction: column;
    align-items: center;
    font-family: "Roboto Condensed", "Arial Narrow", sans-serif;
    font-weight: 400;
    text-transform: uppercase;
  }
  .brand__name {
    display: flex;
    align-items: center;
    gap: 12px;
    font-size: 22px;
    letter-spacing: 0.32em;
  }
  .brand__dot {
    width: 12px;
    height: 12px;
    border-radius: 50%;
  }
  .brand__rule {
    width: 100%;
    height: 1px;
    margin: 8px 0 6px;
  }
  .brand__tagline {
    font-size: 20px;
    letter-spacing: 0.01em;
  }
  .card--front .brand { color: var(--mark-light); }
  .card--front .brand__dot,
  .card--front .brand__rule { background: var(--mark-light); }

  /* Back face */
  .card--back { background: var(--paper); }
  .card__bands {
    position: absolute;
    inset: 0;
    width: 100%;
    height: 100%;
  }
  .card--back .brand {
    position: absolute;
    top: 58px;
    left: 0;
    right: 0;
    color: #5d5d61;
  }
  .card--back .brand__name { font-size: 19px; }
  .card--back .brand__tagline { font-size: 18px; }
  .card--back .brand__dot { background: var(--violet); width: 10px; height: 10px; }
  .card--back .brand__rule { background: #5d5d61; }

  .holder {
    position: absolute;
    left: 22px;
    top: 222px;
    font-family: "Arimo", Arial, sans-serif;
    font-size: 17px;
    line-height: 1.32;
    color: var(--text-grey);
  }
  .holder__name { color: var(--violet); }

  .contact {
    position: absolute;
    right: 22px;
    top: 193px;
    text-align: right;
    font-family: "Arimo", Arial, sans-serif;
    font-size: 17px;
    line-height: 1.32;
    color: var(--text-grey);
    font-style: normal;
  }
  .contact__email { color: var(--violet); }
</style>
</head>
<body>
<main class="sheet">

  <section class="card card--front" aria-label="Frente de la tarjeta">
    <div class="brand">
      <div class="brand__name"><span class="brand__dot"></span>Tomás Rivera</div>
      <div class="brand__rule"></div>
      <div class="brand__tagline">Laboratorio de Procesamiento Histológico</div>
    </div>
  </section>

  <section class="card card--back" aria-label="Dorso de la tarjeta">
    <svg class="card__bands" viewBox="0 0 640 391" preserveAspectRatio="none" aria-hidden="true">
      <polygon points="0,0 330,0 300,50 0,50" fill="var(--grey-band)"/>
      <polygon points="330,0 640,0 640,50 300,50" fill="var(--violet)"/>
      <polygon points="0,50 300,50 296,56 0,56" fill="var(--grey-band-light)"/>
      <polygon points="0,372 250,372 240,391 0,391" fill="var(--violet)"/>
      <polygon points="250,372 640,372 640,391 240,391" fill="var(--grey-band)"/>
    </svg>

    <div class="brand">
      <div class="brand__name"><span class="brand__dot"></span>Tomás Rivera</div>
      <div class="brand__rule"></div>
      <div class="brand__tagline">Laboratorio de Procesamiento Histológico</div>
    </div>

    <div class="holder">
      <p class="holder__role">Técnico en Anatomía Patológica</p>
      <p class="holder__name">Tomás Rivera Ibarra</p>
      <p class="holder__licence">M.P 47203</p>
    </div>

    <address class="contact">
      <p>Av. Paredes Luján 418</p>
      <p>2do piso - Instituto Marbel.</p>
      <p>Córdoba, Argentina</p>
      <p>(0351) 154820937</p>
      <p class="contact__email">rivera.tomas@correolab.example</p>
    </address>
  </section>

</main>
</body>
</html>
```